Realtor / Kitchen & Bath Designer / Curb Appeal Specialist Before & After Postcard

Realtor / Curb Appeal Specialist / Kitchen & Bath Designer / Interior Decorator / Real Estate Staging

I need an oversized postcard to send to luxury / waterfront homes and condominiums. I have a background photo and 3 sets of Before and After photos and a professional photo for my bio which I would like to be on the back with room for address labels and postage.

I offer a FREE (No obligation) in-home design / staging consultation for potential homeowners interesed in selling their home or condominium. I will place some of these cards in open houses, related businesses, some will be direct mailed, some will be handed out.

My goal with this marketing is to attract potential SELLERS who realize that they need my skills, ideas, experience for: Curb Appeal / Facade Enhancement / landscaping ... Kitchen & Bath Updating ... Decorating / Paint Colors ... Staging, etc ... in order to help SELL their properties FASTER and with HIGHER NET PROCEEDS on the real estate market ... and HOPEFULLY LISTING their property with me as their Listing Realtor.

I realize this is a bit complicated but I hopfully the photos will mostly convey the message ... with text as needed, more elegantly than I have worded this. Here are some POINTS that I am trying to make:

Curb Appeal, Landscaping, Updated Kitchens & Baths, Paint Colors, Lighting ... are more important than ever ... to sell upscale waterfront homes/condominiums in this competitive market ... design savvy BUYERS are looking for quality fixtures, features, and WOW factors.

Bio. Orin Faraday is a Florida Realtor and licensed Interior Decorator, Kitchen & Bath Designer, and Curb Appeal Specialist with 25+ years experience in the residential design/remodeling industry.

Photos are: Professional photo (can be cropped and/or B/W with Bio on back) ... Photos are in order: 6 sets of Before - After, with addtional photo.

Target Market(s)

Home and Condo owners who are wanting to SELL their home and hopefully LIST with me as a REALTOR. I also pick up some design work.

Industry/Entity Type

Landscaping

Requirements
Must have
• Front: The entire front could be a faded - muted (half tone) photo of the kitchen (last photo) ... then 3 or 4 sets of smaller before & after pics with borders. The after photos could be slightly larger than the before pics which could be inset or superimposed/offset at the bottom. There should be a lead line at the top such as :

"Serious about selling your home or condominium?" and maybe at the bottom: "Today's design savvy BUYERS desire updated kitchens and baths, quality fixtures, design features, and attractive landscaping."

Back: My bio with photo. Room for hand written or address labels/postage. Perhaps the Before & After of the condo bathroom could also be on the back at the left /top with my photo/bio smaller at the left bottom.
Nice to have
• somehow make it seem classy and elegant ... not like a sales pitch
Should not have
• anything that looks or sounds tacky.

```html
<!DOCTYPE html>
<html lang="en">
<head>
<meta charset="utf-8">
<title>Orin Faraday – Postcard Back</title>
<link rel="stylesheet" href="https://fonts.googleapis.com/css2?family=Raleway:wght@400;600;700&display=swap">
<style>
  :root {
    --page-bg: #e9e7e4;
    --card-bg: #ffffff;
    --brown: #3e2a2c;
    --brown-text: #f3ece6;
    --accent: #e8c9a8;
    --rule: #ddd2c6;
    --address-line: #9a6350;
    --logo-ink: #1f1a1b;
    --logo-square: #9cc1e0;
  }
  * { box-sizing: border-box; margin: 0; padding: 0; }
  html, body {
    width: 1200px; height: 800px; overflow: hidden;
    background: var(--page-bg);
    font-family: "Raleway", sans-serif;
  }
  .postcard {
    position: absolute; left: 70px; top: 25px;
    width: 1060px; height: 750px;
    background: var(--card-bg);
    box-shadow: 0 2px 10px rgba(0,0,0,0.12);
  }
  .brand {
    position: absolute; left: 40px; top: 40px;
    display: flex; align-items: center; gap: 14px;
  }
  .brand-square {
    width: 48px; height: 48px; background: var(--logo-square);
  }
  .brand-name {
    font-size: 30px; font-weight: 600; color: var(--logo-ink); letter-spacing: 0.5px;
  }
  .portrait {
    position: absolute; left: 40px; top: 190px;
    width: 215px; height: 145px;
    background: linear-gradient(135deg, #b89a5a 0%, #6b5a3a 45%, #2a3350 100%);
  }
  .cta-panel {
    position: absolute; left: 40px; top: 339px;
    width: 215px; height: 221px;
    background: var(--brown); color: var(--brown-text);
    padding: 22px 18px;
    font-size: 15px; line-height: 1.4;
  }
  .cta-panel strong { font-weight: 700; }
  .cta-phone { margin-top: 12px; font-weight: 700; font-size: 16px; color: var(--accent); }
  .cta-email { font-size: 12.5px; margin-top: 2px; }
  .bio-panel {
    position: absolute; left: 259px; top: 190px;
    width: 381px; height: 370px;
    background: var(--brown); color: var(--brown-text);
    padding: 24px 26px;
    font-size: 15.5px; line-height: 1.42;
  }
  .bio-panel p + p { margin-top: 14px; }
  .bio-name { font-weight: 700; color: #ffffff; }
  .rule-bottom {
    position: absolute; left: 40px; right: 40px; top: 700px;
    height: 2px; background: var(--rule);
  }
  .rule-side {
    position: absolute; left: 40px; top: 560px;
    width: 2px; height: 140px; background: var(--rule);
  }
  .address-lines {
    position: absolute; left: 660px; top: 400px;
  }
</style>
</head>
<body>
  <main class="postcard">
    <div class="brand">
      <span class="brand-square"></span>
      <span class="brand-name">Bayfront Realty</span>
    </div>

    <div class="portrait" role="img" aria-label="Professional portrait photo of Orin Faraday"></div>

    <section class="cta-panel">
      <p>Call or email today to schedule a <strong>FREE</strong> In-home Kitchen &amp; Bath / Curb Appeal / Real Estate Staging Consultation.</p>
      <p class="cta-phone">(850) 555-0147</p>
      <p class="cta-email">orinsellshomes@mail.com</p>
    </section>

    <section class="bio-panel">
      <p><span class="bio-name">Orin Faraday</span> is a Florida Realtor and licensed Interior Decorator, Kitchen &amp; Bath Designer, and Curb Appeal Specialist with 25+ years experience in the residential design/ remodeling industry and 14 years as a Pensacola area real estate agent, working with Buyers, Sellers, Investors, and Real Estate/ Design professionals.</p>
      <p>Orin has the knowledge, skills, creative ideas, practical experience, and proven track record for enhancing your home's overall QUALITY and APPEAL, which will SELL your home more quickly at a significantly HIGHER SALES PRICE!</p>
    </section>

    <div class="rule-side"></div>
    <div class="rule-bottom"></div>

    <svg class="address-lines" width="340" height="240" viewBox="0 0 340 240" aria-hidden="true">
      <g stroke="var(--address-line)" stroke-width="2.5">
        <line x1="0" y1="20" x2="340" y2="20"/>
        <line x1="0" y1="85" x2="340" y2="85"/>
        <line x1="0" y1="150" x2="340" y2="150"/>
        <line x1="0" y1="215" x2="340" y2="215"/>
      </g>
    </svg>
  </main>
</body>
</html>
```